Coral Ridge Networks Ltd

I need a website that is an informational only. We are a construction business building telecommunications sites. Seeing how our company is Coral Ridge the color blue might want to be incorporated in the color scheme.
I can provide more picture of towers and wireless communications if needed.
current website www.coralridgenet.ca

Industry/Entity Type

Wireless Telecommunications, Construction

Coding

Coded - Design and coding required

Number of Pages Required

2 page

Font styles to use
Sans Serif

Colors

Designer to choose colors to be used in the design.

```html
<!DOCTYPE html>
<html lang="en">
<head>
<meta charset="utf-8">
<title>Coral Ridge Networks Ltd</title>
<link href="https://fonts.googleapis.com/css2?family=Poppins:wght@400;500;600;700&display=swap" rel="stylesheet">
<style>
:root{
  --navy:#16227a;
  --navy-deep:#0e1757;
  --blue:#2443c4;
  --sky:#5aaee8;
  --sky-soft:#9fd0f3;
  --wash:#edf4fc;
  --ink:#2a2f45;
  --muted:#6b7288;
  --line:#d4dbe8;
  --white:#ffffff;
}
*{box-sizing:border-box;margin:0;padding:0}
html,body{width:1200px;height:3888px;overflow:hidden}
body{font-family:"Poppins",sans-serif;color:var(--ink);background:var(--white);position:relative}
.abs{position:absolute}
.brand{font-family:"Poppins",sans-serif;font-weight:700;color:var(--blue);letter-spacing:.5px}
.btn{position:absolute;display:flex;align-items:center;justify-content:center;border-radius:30px;font-size:15px;font-weight:500;color:var(--white);background:var(--sky)}
.btn-outline{background:transparent;border:2px solid var(--sky);color:var(--sky)}
.section-title{position:absolute;left:0;width:1200px;text-align:center;font-size:46px;font-weight:700;color:var(--navy)}

/* header */
.site-header{left:0;top:0;width:1200px;height:96px;background:var(--white);z-index:5}
.site-header .brand{left:88px;top:24px;font-size:34px}
.main-nav{left:380px;top:36px;display:flex;gap:40px;font-size:15px;font-weight:500;color:var(--navy)}
.main-nav .active{color:var(--sky);border-bottom:2px solid var(--sky);padding-bottom:4px}
.site-header .btn{left:968px;top:26px;width:140px;height:42px}

/* hero */
.hero{left:0;top:96px;width:1200px;height:640px;background:linear-gradient(100deg,#0f1a5e 0%,#1c2f96 45%,#3b5fc4 75%,#8fb6e4 100%)}
.hero-eyebrow{left:88px;top:174px;font-size:24px;color:var(--white)}
.hero-title{left:88px;top:214px;font-size:50px;font-weight:700;line-height:1.18;color:var(--white)}
.hero-btn{left:88px;top:350px;width:130px;height:38px;color:var(--white);border-color:var(--white)}
.hero-dots{left:680px;top:430px;display:flex;gap:12px}
.hero-dots span{width:14px;height:14px;border-radius:50%;border:2px solid var(--white)}
.hero-dots span.on{background:var(--white)}

/* safety */
.safety-brand{left:120px;top:840px;font-size:84px;line-height:1.15}
.safety-title{left:472px;top:790px;font-size:42px;font-weight:700;line-height:1.2;color:var(--navy)}
.safety-text{left:472px;top:905px;width:560px;font-size:14px;line-height:1.7;color:var(--muted)}
.safety-text p+p{margin-top:10px}
.safety-btn{left:472px;top:1068px;width:130px;height:38px}

/* services */
.services-bg{left:0;top:1150px;width:1200px;height:900px}
.card-img{position:absolute}
.card-cap{position:absolute;background:var(--white);padding:22px 26px;box-shadow:10px 10px 0 var(--navy)}
.card-cap h3{font-size:22px;font-weight:600;color:var(--ink);margin-bottom:10px}
.card-cap p{font-size:13px;line-height:1.6;color:var(--muted)}

/* clients */
.client-row{left:150px;top:2250px;width:900px;display:flex;justify-content:space-between}
.client{width:190px;height:86px;display:flex;align-items:center;justify-content:center;gap:8px;font-size:15px;font-weight:600;color:var(--navy);text-align:center}
.client i{width:14px;height:14px;border-radius:50%;background:var(--navy);flex:none}
.arrow{width:34px;height:34px;border-radius:50%;border:2px solid var(--sky);display:flex;align-items:center;justify-content:center;background:var(--white)}

/* testimonials */
.testi{position:absolute;top:2640px;width:310px}
.testi .quote{font-size:60px;line-height:40px;font-weight:700;color:var(--blue)}
.testi .box{background:var(--white);padding:20px 22px;font-size:14px;line-height:1.7;color:var(--muted);margin-top:6px}
.testi .who{display:flex;align-items:center;gap:16px;margin-top:16px;font-size:14px;color:var(--blue)}
.avatar{width:58px;height:58px;border-radius:50%;background:linear-gradient(135deg,#c9a48a,#6c5544)}

/* inquiry */
.field{position:absolute}
.field label{display:block;font-size:13px;color:var(--ink);margin-bottom:8px}
.field .input{height:46px;border:1px solid var(--line);border-radius:4px;display:flex;align-items:center;padding-left:14px}
.field .input i{width:12px;height:12px;border-radius:50%;border:1.5px solid #aab3c5}

/* footer */
.footer{left:0;top:3470px;width:1200px;height:378px;background:var(--navy-deep)}
.footer-logo{left:88px;top:3560px;width:170px;height:80px;background:var(--white);display:flex;align-items:center;justify-content:center;font-size:26px}
.footer-heading{position:absolute;font-size:20px;font-weight:600;color:var(--sky)}
.footer-text{position:absolute;font-size:13px;line-height:1.7;color:#d7def2}
.footer-text b{display:block;color:var(--sky);font-weight:500}
.quick-links{left:616px;top:3616px;font-size:14px;line-height:2;color:var(--white)}
.map{left:812px;top:3572px;width:300px;height:210px;background:linear-gradient(135deg,#dfe8d8,#c8d9ea)}
.bottom-bar{left:0;top:3848px;width:1200px;height:40px;background:#0a1245;color:#c6cde6;font-size:13px;display:flex;align-items:center;padding:0 88px;justify-content:space-between}
.social{display:flex;gap:10px;margin-right:60px}
.social span{width:20px;height:20px;border-radius:3px;background:#34407e}
.chat{left:1136px;top:3832px;width:44px;height:44px;border-radius:50%;background:var(--sky)}
</style>
</head>
<body>

<header class="site-header abs">
  <div class="brand abs">Coral Ridge</div>
  <nav class="main-nav abs">
    <span class="active">Home</span><span>About Us</span><span>Safety</span><span>Services</span><span>Careers</span><span>Contact Us</span>
  </nav>
  <div class="btn">Inquiry Now</div>
</header>

<section class="hero abs" role="img" aria-label="Telecommunications tower with antennas and a microwave dish against a blue sky">
  <div class="hero-eyebrow abs">All Coral Ridge Employees are Certified</div>
  <div class="hero-title abs">Tower Competent Climber<br>and Rescue</div>
  <div class="btn btn-outline hero-btn">Contact Us</div>
  <div class="hero-dots abs"><span class="on"></span><span></span><span></span></div>
</section>
<svg class="abs" style="left:0;top:620px" width="1200" height="140" viewBox="0 0 1200 140" preserveAspectRatio="none" aria-hidden="true">
  <path d="M0 70 C300 140 700 130 1200 20 L1200 140 L0 140Z" fill="var(--sky-soft)" opacity=".7"/>
  <path d="M0 90 C320 150 760 140 1200 50 L1200 140 L0 140Z" fill="var(--white)"/>
</svg>

<section class="safety">
  <div class="brand safety-brand abs">Coral<br>Ridge</div>
  <h2 class="safety-title abs">Safety is our core<br>priority what we do</h2>
  <div class="safety-text abs">
    <p>At Coral Ridge Networks Ltd safety is number one. Coral Ridge Networks Ltd is committed to a strong safety policy, protecting its staff and the general public from accidents and harm. All Coral Ridge Employees are certified “Tower Competent Climber and Rescue”.</p>
    <p>In addition to tower safety and fall protection Coral Ridge’s safety training and practices include but are not limited to the following:</p>
  </div>
  <div class="btn btn-outline safety-btn">Read More</div>
</section>

<svg class="services-bg abs" viewBox="0 0 1200 900" preserveAspectRatio="none" aria-hidden="true">
  <path d="M0 60 C300 0 800 120 1200 40 L1200 860 C800 900 400 820 0 880Z" fill="var(--wash)"/>
</svg>
<h2 class="section-title" style="top:1290px;left:100px;width:auto">Our Services</h2>

<div class="card-img" role="img" aria-label="Cellular antenna mast against a bright sky" style="left:572px;top:1252px;width:528px;height:300px;background:linear-gradient(160deg,#b9d7f2,#5f8fc9)"></div>
<div class="card-cap" style="left:640px;top:1470px;width:450px">
  <h3>Towers and Monopoles</h3>
  <p>Coral Ridge has engineered, supplied and installed all your tower needs. New structures or existing, call us for pricing we would be happy to help out.</p>
</div>

<div class="card-img" role="img" aria-label="Brick rooftop with antenna equipment mounted on a building" style="left:100px;top:1392px;width:400px;height:330px;background:linear-gradient(160deg,#c9b8a6,#7d6b5c)"></div>
<div class="card-cap" style="left:100px;top:1690px;width:400px">
  <h3>Rooftop Sites</h3>
  <p>Structural upgrades or simple ballast mounts. Wether on the ground, ballasted build outs or cabinets on the roof, Coral Ridge can install what you need where you need it.</p>
</div>

<div class="card-img" role="img" aria-label="Floor plan drawing for an in-building antenna system" style="left:572px;top:1624px;width:528px;height:240px;background:linear-gradient(160deg,#e7ebf1,#a8b4c6)"></div>
<div class="card-cap" style="left:572px;top:1830px;width:440px">
  <h3>In Building</h3>
  <p>Small office or large mall. Coral Ridge has installed services into all size buildings. Fiber, radio or coax, we have the abilities to install, test and get the job done.</p>
</div>
<div class="btn" style="left:100px;top:1900px;width:140px;height:40px">Contact Us</div>

<h2 class="section-title" style="top:2150px">Our Clients</h2>
<div class="arrow abs" style="left:96px;top:2276px"><svg width="12" height="12" viewBox="0 0 12 12"><path d="M8 1 3 6l5 5" stroke="var(--sky)" stroke-width="2" fill="none"/></svg></div>
<div class="client-row abs">
  <div class="client"><i></i>Northvale Motors</div>
  <div class="client"><i></i>Kestrel Systems</div>
  <div class="client"><i></i>Greenlea</div>
  <div class="client"><i></i>Lakeshore Invest</div>
</div>
<div class="arrow abs" style="left:1070px;top:2276px"><svg width="12" height="12" viewBox="0 0 12 12"><path d="M4 1l5 5-5 5" stroke="var(--sky)" stroke-width="2" fill="none"/></svg></div>

<svg class="abs" style="left:0;top:2390px" width="1200" height="600" viewBox="0 0 1200 600" preserveAspectRatio="none" aria-hidden="true">
  <path d="M0 80 C300 0 800 140 1200 60 L1200 540 C800 600 400 510 0 580Z" fill="var(--wash)"/>
</svg>
<h2 class="section-title" style="top:2550px">Testimonials</h2>
<div class="arrow abs" style="left:46px;top:2740px"><svg width="12" height="12" viewBox="0 0 12 12"><path d="M8 1 3 6l5 5" stroke="var(--sky)" stroke-width="2" fill="none"/></svg></div>
<div class="testi" style="left:100px">
  <div class="quote">“</div>
  <div class="box">Lorem Ipsum is simply dummy text of the printing and typesetting industry. Lorem Ipsum has been the industry’s standard dummy text ever since the 1500s, when an unknown printer took a galley.</div>
  <div class="who"><span class="avatar" role="img" aria-label="Client portrait"></span>Marina K., Aug 22</div>
</div>
<div class="testi" style="left:450px">
  <div class="quote">“</div>
  <div class="box">Lorem Ipsum is simply dummy text of the printing and typesetting industry. Lorem Ipsum has been the industry’s standard dummy text ever since the 1500s, when an unknown printer took a galley.</div>
  <div class="who"><span class="avatar" role="img" aria-label="Client portrait"></span>Marina K., Aug 22</div>
</div>
<div class="testi" style="left:800px">
  <div class="quote">“</div>
  <div class="box">Lorem Ipsum is simply dummy text of the printing and typesetting industry. Lorem Ipsum has been the industry’s standard dummy text ever since the 1500s, when an unknown printer took a galley.</div>
  <div class="who"><span class="avatar" role="img" aria-label="Client portrait"></span>Marina K., Aug 22</div>
</div>
<div class="arrow abs" style="left:1128px;top:2740px"><svg width="12" height="12" viewBox="0 0 12 12"><path d="M4 1l5 5-5 5" stroke="var(--sky)" stroke-width="2" fill="none"/></svg></div>

<h2 class="section-title" style="top:3060px">Quick Inquiry</h2>
<div class="field" style="left:165px;top:3160px;width:275px"><label>Full Name</label><div class="input"><i></i></div></div>
<div class="field" style="left:465px;top:3160px;width:275px"><label>Last Name</label><div class="input"><i></i></div></div>
<div class="field" style="left:760px;top:3160px;width:275px"><label>Your Message</label><div class="input" style="height:126px;align-items:flex-start;padding-top:16px"><i></i></div></div>
<div class="field" style="left:165px;top:3240px;width:275px"><label>Phone Number</label><div class="input"><i></i></div></div>
<div class="field" style="left:465px;top:3240px;width:275px"><label>Your Email</label><div class="input"><i></i></div></div>
<div class="btn btn-outline" style="left:535px;top:3350px;width:130px;height:38px">Submit</div>

<svg class="abs" style="left:0;top:3400px" width="1200" height="90" viewBox="0 0 1200 90" preserveAspectRatio="none" aria-hidden="true">
  <path d="M0 40 C400 110 800 0 1200 30 L1200 90 L0 90Z" fill="var(--sky)"/>
  <path d="M0 60 C400 120 800 20 1200 60 L1200 90 L0 90Z" fill="var(--navy-deep)"/>
</svg>
<footer class="footer abs"></footer>
<div class="footer-logo abs brand">Coral Ridge</div>
<div class="footer-heading" style="left:88px;top:3656px">About Us</div>
<div class="footer-text" style="left:88px;top:3692px;width:220px">At Coral Ridge Networks Ltd, we are dedicated to providing our customers with friendly, reliable service.</div>
<div class="footer-heading" style="left:350px;top:3572px">Contact Info</div>
<div class="footer-text" style="left:350px;top:3614px;width:230px">
  <b>Call us :</b>
  <div>1-604-555-0142</div>
  <div style="margin-top:8px">info@coralridgenet.ca</div>
  <b style="margin-top:14px">Address :</b>
  <div>4120 Harbour Rd, Langley, BC<br>V2Y 0B4</div>
</div>
<div class="footer-heading" style="left:616px;top:3572px">Quick Link</div>
<div class="quick-links abs">Home<br>About Us<br>Safety<br>Services<br>Careers<br>Contact Us</div>
<div class="map abs" role="img" aria-label="Street map showing the office location"></div>
<div class="bottom-bar abs">
  <span>© Copyright 2022 Coral Ridge. All Rights Reserved.</span>
  <div class="social"><span></span><span></span><span></span><span></span></div>
</div>
<div class="chat abs"></div>

</body>
</html>
```